Dalwin Electric Supply, Inc. Business Card Design

We are an Electrical Distributor looking for a Modern, Professional Business Card design.

Target Market(s)

Residential Commercial Industrial

Industry/Entity Type

Electrical

Contact Information for Business Card

Dalwin Electric Supply, Inc.
418 Tallow Creek Road
Brennick, NC 27514
555-312-4867
555-312-4921 Fax
dalwinelectric@voltmail.example

```html
<!DOCTYPE html>
<html lang="en">
<head>
<meta charset="utf-8">
<title>Dalwin Electric Supply, Inc. – Business Card</title>
<link rel="stylesheet" href="https://fonts.googleapis.com/css2?family=Source+Sans+3:wght@400;600&display=swap">
<style>
  :root {
    --backdrop: #e9e7e3;
    --card-white: #ffffff;
    --brand-blue: #1a78c2;
    --brand-blue-deep: #0f65ad;
    --brand-blue-light: #3d93d6;
    --ink: #5b5f63;
    --ink-soft: #8a8e92;
    --on-blue: #ffffff;
  }
  * { box-sizing: border-box; margin: 0; padding: 0; }
  html, body {
    width: 1200px;
    height: 1023px;
    overflow: hidden;
    background: var(--backdrop);
    font-family: "Source Sans 3", Arial, sans-serif;
  }
  .stage { position: relative; width: 1200px; height: 1023px; }
  .card {
    position: absolute;
    width: 630px;
    height: 360px;
    border-radius: 4px;
    box-shadow: 0 10px 28px rgba(0,0,0,0.18);
    overflow: hidden;
  }

  /* Front side */
  .card-front {
    left: 70px;
    top: 80px;
    background: var(--card-white);
  }
  .front-brand {
    position: absolute;
    left: 44px;
    top: 150px;
    display: flex;
    align-items: center;
    gap: 12px;
  }
  .brand-square {
    width: 18px;
    height: 18px;
    background: var(--brand-blue);
  }
  .brand-name {
    font-size: 22px;
    font-weight: 600;
    color: var(--brand-blue);
    letter-spacing: 0.5px;
  }
  .contact {
    position: absolute;
    left: 376px;
    top: 96px;
    color: var(--ink);
  }
  .person-name {
    font-size: 20px;
    font-weight: 600;
    color: var(--brand-blue);
    letter-spacing: 1.5px;
    text-transform: uppercase;
  }
  .person-role {
    font-size: 15px;
    color: var(--ink-soft);
    margin: 4px 0 14px;
  }
  .contact-line {
    display: flex;
    align-items: center;
    gap: 8px;
    font-size: 15px;
    line-height: 24px;
  }
  .contact-line svg { width: 14px; height: 14px; fill: var(--brand-blue); flex: none; }
  .address { margin-top: 12px; font-size: 15px; line-height: 24px; }

  /* Back side */
  .card-back {
    left: 500px;
    top: 580px;
    background: linear-gradient(135deg, var(--brand-blue-light) 0%, var(--brand-blue) 45%, var(--brand-blue-deep) 100%);
  }
  .back-texture {
    position: absolute;
    inset: 0;
    background: linear-gradient(160deg, rgba(255,255,255,0.08) 0%, rgba(255,255,255,0) 55%, rgba(0,0,0,0.06) 100%);
  }
  .back-brand {
    position: absolute;
    inset: 0;
    display: flex;
    align-items: center;
    justify-content: center;
    gap: 14px;
  }
  .back-brand .brand-square { background: var(--on-blue); width: 20px; height: 20px; }
  .back-brand .brand-name { color: var(--on-blue); font-size: 26px; }
</style>
</head>
<body>
<main class="stage">

  <section class="card card-front" aria-label="Business card front">
    <div class="front-brand">
      <span class="brand-square"></span>
      <span class="brand-name">Dalwin Electric Supply, Inc.</span>
    </div>

    <div class="contact">
      <p class="person-name">Mara Quillon</p>
      <p class="person-role">Director</p>

      <p class="contact-line">
        <svg viewBox="0 0 16 16" aria-hidden="true"><path d="M3 1h3l1.5 4-2 1.3a9 9 0 0 0 4.2 4.2L11 8.5l4 1.5v3a2 2 0 0 1-2 2A12 12 0 0 1 1 3a2 2 0 0 1 2-2z"/></svg>
        555-312-4867
      </p>
      <p class="contact-line">
        <svg viewBox="0 0 16 16" aria-hidden="true"><path d="M4 1h7v4H4zM2 6h12a1 1 0 0 1 1 1v6a1 1 0 0 1-1 1H2a1 1 0 0 1-1-1V7a1 1 0 0 1 1-1zm2 5v4h8v-4z"/></svg>
        555-312-4921
      </p>
      <p class="contact-line">
        <svg viewBox="0 0 16 16" aria-hidden="true"><path d="M1 3h14v10H1zm1.5 1.2L8 8.6l5.5-4.4z"/></svg>
        dalwinelectric@voltmail.example
      </p>

      <p class="address">418 Tallow Creek Road<br>Brennick, NC 27514</p>
    </div>
  </section>

  <section class="card card-back" aria-label="Business card back">
    <div class="back-texture" role="img" aria-label="Soft blue faceted background"></div>
    <div class="back-brand">
      <span class="brand-square"></span>
      <span class="brand-name">Dalwin Electric Supply, Inc.</span>
    </div>
  </section>

</main>
</body>
</html>
```